Social Health & Parkinson's

I need a 1-pg horizontal infographic that can be handed out to patients and providers. It needs to be scientifically sound (data provided), easy to understand, and visually pleasing. Target audience; patiens (mostly 40-90 years old) and providers (neurologists, nurses, physical therapists, naturopathic physicians, support group leaders, etc.) We need 6 of these, one for each topic listed on the website. Ideally, we'll hire the winner for 5 more similar projects and keep a theme.

Target Market(s)

Patients with Parkinson's disease, their families, care providers. To be handed out by physicians, support group leaders, etc.

Colors

Designer to choose colors to be used in the design.

Requirements
Must have
• Visually stunning. Data integrity-- keep the numbers and the figures we provide. Reference to where the data is coming from. Be thoughtful of elderly, vision issues. Teach everyone something.

```html
<!DOCTYPE html>
<html lang="en">
<head>
<meta charset="utf-8">
<title>Social Health &amp; Parkinson's</title>
<link href="https://fonts.googleapis.com/css2?family=Montserrat:ital,wght@0,400;0,500;0,600;0,700;0,800;1,500&family=Fira+Sans+Condensed:wght@400;500;600;700&family=Lato:wght@400;700&display=swap" rel="stylesheet">
<style>
:root{
  --paper:#eef0ed;
  --navy:#1d3f5e;
  --navy-deep:#1f2a5a;
  --slate:#535e7a;
  --rose:#d06c82;
  --rose-soft:#e08a9a;
  --rose-tint:#f6e6e8;
  --bar-mid:#54627e;
  --ink:#333;
  --rule:#7a8596;
  --white:#fff;
  --muted:#c8ccd2;
}
*{box-sizing:border-box;margin:0;padding:0}
html,body{width:1200px;height:848px;overflow:hidden;background:var(--paper)}
body{position:relative;font-family:"Montserrat",sans-serif;color:var(--navy)}
.abs{position:absolute}
.top-band{left:253px;top:0;width:694px;height:18px;background:var(--slate)}
.title{left:0;width:1200px;top:25px;text-align:center;font-weight:800;font-size:20.5px;color:var(--rose);letter-spacing:.2px}
.title .accent{color:var(--navy)}
.timeline{left:250px;top:78px;width:700px;height:52px}
.topic-label{left:432px;top:116px;width:200px;text-align:center;font-size:9.5px;font-weight:700;color:var(--rose);letter-spacing:.5px}
.tagline-rule{top:179px;height:1px;background:var(--rose-soft)}
.tagline{left:350px;width:502px;top:166px;text-align:center;white-space:nowrap;font-style:italic;font-weight:500;font-size:18px;letter-spacing:.3em;color:var(--navy)}
.photo{left:54px;top:205px;width:143px;height:143px;background:linear-gradient(160deg,#d57f92,#c9677d)}
.progress-card{left:44px;top:361px;width:154px;height:152px;background:repeating-linear-gradient(135deg,#9aa0a6 0 3px,transparent 3px 7px)}
.progress-card .inner{position:absolute;left:8px;top:0;width:146px;height:143px;background:var(--paper);box-shadow:0 0 3px rgba(0,0,0,.12)}
.progress-head{left:60px;top:366px;font-weight:700;font-size:11px;line-height:11.5px;color:var(--navy)}
.progress-foot{left:100px;top:472px;width:92px;text-align:right;font-weight:700;font-size:11px;line-height:10.5px;color:var(--rose)}
.vrule{width:1px;background:var(--rule)}
.hrule{height:1px;background:var(--rule)}
.panel{background:var(--white)}
.sub-head{font-size:11.5px;font-weight:500;color:var(--rose);letter-spacing:.2px;white-space:nowrap}
.claim{font-weight:700;font-size:17px;color:var(--navy);white-space:nowrap}
.finding{left:446px;top:430px;width:389px;height:87px;background:var(--rose-tint);padding:3px 6px;font-family:"Fira Sans Condensed",sans-serif;font-weight:500;font-size:15px;line-height:19.7px;color:var(--rose);white-space:nowrap}
.summary{left:762px;top:562px;width:430px;font-weight:700;font-size:25.5px;line-height:29.4px;color:var(--navy);white-space:nowrap}
.brand{left:990px;top:758px;width:170px;display:flex;align-items:center;gap:6px;justify-content:flex-end}
.brand .dot{width:26px;height:26px;border-radius:50%;background:#b52a35;flex:none}
.brand .name{font-weight:700;font-size:11px;line-height:12px;color:#b52a35}
svg text{font-family:"Lato",sans-serif}
.cond{font-family:"Fira Sans Condensed",sans-serif}
</style>
</head>
<body>

<div class="abs top-band"></div>
<h1 class="abs title">CORELATION BETWEEN LIFE STYLE AND <span class="accent">PARKINSON'S</span> DISEASE</h1>

<svg class="abs timeline" viewBox="0 0 700 52" role="img" aria-label="Topic timeline: medication, nutrition, social health, assessment, exercise, sleep">
  <line x1="14" y1="34" x2="686" y2="34" stroke="#3d5876" stroke-width="1.2"/>
  <g fill="#3d5876">
    <circle cx="14" cy="34" r="2.6"/><circle cx="148" cy="34" r="2.6"/><circle cx="282" cy="34" r="2.6"/>
    <circle cx="417" cy="34" r="2.6"/><circle cx="552" cy="34" r="2.6"/><circle cx="686" cy="34" r="2.6"/>
  </g>
  <g fill="#d9c9cf" stroke="#b9bfc8" stroke-width="1">
    <rect x="4" y="8" width="18" height="20" rx="4"/>
    <rect x="138" y="6" width="14" height="20" rx="3"/><circle cx="155" cy="20" r="6"/>
    <rect x="406" y="6" width="18" height="22" rx="2"/><circle cx="423" cy="22" r="5"/>
    <rect x="538" y="6" width="26" height="14" rx="5"/>
  </g>
  <g>
    <circle cx="282" cy="14" r="7" fill="var(--navy)"/>
    <rect x="266" y="18" width="32" height="12" rx="6" fill="var(--navy)"/>
    <circle cx="282" cy="15" r="4.5" fill="var(--rose)"/>
    <rect x="274" y="20" width="16" height="9" rx="4" fill="var(--rose)"/>
  </g>
  <path d="M690 6a11 11 0 1 0 8 16a9 9 0 0 1 -8 -16z" fill="#ecdfe3" stroke="#b9bfc8" stroke-width="1"/>
</svg>
<div class="abs topic-label">SOCIAL HEALTH</div>

<div class="abs tagline-rule" style="left:0;width:350px"></div>
<div class="abs tagline-rule" style="left:852px;width:348px"></div>
<p class="abs tagline">Make friends . Avoid loneliness</p>

<div class="abs photo" role="img" aria-label="Silhouette of a person standing apart from a faded crowd, in rose and navy"></div>

<div class="abs progress-card"><div class="inner"></div></div>
<p class="abs progress-head">progression of<br>parkinson's disease</p>
<svg class="abs" style="left:74px;top:395px" width="100" height="74" viewBox="0 0 100 74" aria-hidden="true">
  <path d="M2 24 L26 0 L50 24 L39 24 L39 62 L13 62 L13 24Z" fill="var(--navy)"/>
  <path d="M60 12 L86 12 L86 46 L98 46 L73 72 L48 46 L60 46Z" fill="var(--rose)"/>
</svg>
<p class="abs progress-foot">decreased<br>social health</p>

<div class="abs vrule" style="left:214px;top:212px;height:282px"></div>

<svg class="abs panel" style="left:232px;top:205px" width="184" height="141" viewBox="0 0 352 269" role="img" aria-label="PRO-PD score by social satisfaction rating">
  <rect x="8" y="8" width="336" height="253" fill="none" stroke="#dde0e4" stroke-width="2"/>
  <g font-weight="700" font-size="10.5" text-anchor="middle" fill="#222">
    <text x="176" y="30">In general, please rate how well you rate your</text>
    <text x="176" y="42">satisfaction with your social activities and</text>
    <text x="176" y="54">relationships</text>
  </g>
  <line x1="64" y1="68" x2="64" y2="179" stroke="#444"/>
  <line x1="64" y1="179" x2="330" y2="179" stroke="#444"/>
  <g font-size="7.5" font-weight="700" text-anchor="end" fill="#222">
    <text x="58" y="182">0</text><text x="58" y="154">500</text><text x="58" y="126">1000</text><text x="58" y="99">1500</text><text x="58" y="71">2000</text>
  </g>
  <text transform="translate(33 124) rotate(-90)" font-size="8" font-weight="700" text-anchor="middle">PRO-PD</text>
  <rect x="74" y="152" width="32" height="27" fill="var(--navy)"/>
  <rect x="128" y="142" width="32" height="37" fill="var(--navy)"/>
  <rect x="181" y="130" width="32" height="49" fill="var(--navy)"/>
  <rect x="234" y="114" width="32" height="65" fill="var(--bar-mid)"/>
  <rect x="288" y="106" width="32" height="73" fill="#2f4f70"/>
  <g font-size="8" text-anchor="middle" fill="#222">
    <text x="90" y="147">494</text><text x="144" y="137">667</text><text x="197" y="125">889</text><text x="250" y="109">1178</text><text x="304" y="101">1317</text>
  </g>
  <g font-size="7" font-weight="700" text-anchor="end" fill="#222">
    <text transform="translate(94 190) rotate(-45)">Excellent (n=343)</text>
    <text transform="translate(148 190) rotate(-45)">Very Good (n=807)</text>
    <text transform="translate(201 190) rotate(-45)">Good (n=468)</text>
    <text transform="translate(254 190) rotate(-45)">Fair (n=289)</text>
    <text transform="translate(308 190) rotate(-45)">Poor (n=61)</text>
  </g>
  <text x="188" y="246" font-size="8.5" font-weight="700" text-anchor="middle">Social Satisfaction</text>
</svg>

<svg class="abs panel" style="left:232px;top:360px" width="181" height="141" viewBox="0 0 346 270" role="img" aria-label="PRO-PD score by social performance rating">
  <rect x="8" y="4" width="330" height="256" fill="none" stroke="#dde0e4" stroke-width="2"/>
  <g font-weight="700" font-size="10.5" text-anchor="middle" fill="#222">
    <text x="176" y="22">In general, please rate how well you carry out</text>
    <text x="176" y="35">your social activities and roles</text>
  </g>
  <line x1="61" y1="48" x2="61" y2="170" stroke="#444"/>
  <line x1="61" y1="170" x2="330" y2="170" stroke="#444"/>
  <g font-size="7.5" font-weight="700" text-anchor="end" fill="#222">
    <text x="55" y="173">0</text><text x="55" y="142">500</text><text x="55" y="112">1000</text><text x="55" y="81">1500</text><text x="55" y="51">2000</text>
  </g>
  <text transform="translate(30 110) rotate(-90)" font-size="8" font-weight="700" text-anchor="middle">PRO-PD</text>
  <rect x="71" y="143" width="32" height="27" fill="var(--navy)"/>
  <rect x="125" y="130" width="32" height="40" fill="var(--navy)"/>
  <rect x="178" y="114" width="32" height="56" fill="var(--navy)"/>
  <rect x="232" y="95" width="32" height="75" fill="var(--bar-mid)"/>
  <rect x="285" y="81" width="32" height="89" fill="#2f4f70"/>
  <g font-size="8" text-anchor="middle" fill="#222">
    <text x="87" y="138">446</text><text x="141" y="125">653</text><text x="194" y="109">922</text><text x="248" y="90">1233</text><text x="301" y="76">1464</text>
  </g>
  <g font-size="7" font-weight="700" text-anchor="end" fill="#222">
    <text transform="translate(91 181) rotate(-45)">Excellent (n=322)</text>
    <text transform="translate(145 181) rotate(-45)">Very Good (n=647)</text>
    <text transform="translate(198 181) rotate(-45)">Good (n=491)</text>
    <text transform="translate(252 181) rotate(-45)">Fair (n=267)</text>
    <text transform="translate(305 181) rotate(-45)">Poor (n=44)</text>
  </g>
  <text x="186" y="237" font-size="8.5" font-weight="700" text-anchor="middle">Social Performance</text>
</svg>

<div class="abs vrule" style="left:432px;top:212px;height:512px"></div>

<p class="abs sub-head" style="left:450px;top:206px">modifiable variables assoiciated with risk of Parkinson's disease</p>

<svg class="abs panel" style="left:448px;top:223px" width="395" height="165" viewBox="0 0 755 315" role="img" aria-label="Change in PRO-PD score by modifiable lifestyle variable">
  <g stroke="#e4e6ea" stroke-width="1">
    <line x1="208" y1="0" x2="208" y2="290"/><line x1="269" y1="0" x2="269" y2="290"/><line x1="330" y1="0" x2="330" y2="290"/>
    <line x1="391" y1="0" x2="391" y2="290"/><line x1="452" y1="0" x2="452" y2="290"/><line x1="513" y1="0" x2="513" y2="290"/>
    <line x1="574" y1="0" x2="574" y2="290"/><line x1="635" y1="0" x2="635" y2="290"/><line x1="697" y1="0" x2="697" y2="290"/>
  </g>
  <g fill="var(--rose)">
    <rect x="268" y="6" width="184" height="10"/>
    <rect x="274" y="33" width="178" height="10"/>
    <rect x="307" y="59" width="145" height="10"/>
    <rect x="312" y="85" width="140" height="10"/>
    <rect x="335" y="111" width="117" height="10"/>
    <rect x="349" y="138" width="103" height="10"/>
    <rect x="363" y="164" width="89" height="10"/>
    <rect x="423" y="190" width="29" height="10"/>
    <rect x="452" y="217" width="85" height="10"/>
    <rect x="452" y="243" width="110" height="10"/>
    <rect x="452" y="269" width="200" height="10"/>
  </g>
  <g font-size="8" fill="var(--rose)" text-anchor="end" class="cond">
    <text x="197" y="14">Exercise 30+ min/d, 7 days/ wk</text>
    <text x="197" y="41">Exercise 30+ min/d, 6 days/ wk</text>
    <text x="197" y="67">Exercise 30+ min/d, 5 days/ wk</text>
    <text x="197" y="93">Exercise 30+ min/d, 4 days/ wk</text>
    <text x="197" y="119">Exercise 30+ min/d, 3 days/ wk</text>
    <text x="197" y="146">I have lots of friends</text>
    <text x="197" y="172">I cook most of my meals</text>
    <text x="197" y="198">I practice stress management</text>
    <text x="197" y="225">I am overweight</text>
    <text x="197" y="251">I have a lot of stress</text>
    <text x="197" y="277">I am lonely</text>
  </g>
  <g font-size="8" fill="var(--rose)">
    <text x="262" y="14" text-anchor="end">-301</text>
    <text x="268" y="41" text-anchor="end">-292</text>
    <text x="301" y="67" text-anchor="end">-237</text>
    <text x="306" y="93" text-anchor="end">-229</text>
    <text x="329" y="119" text-anchor="end">-192</text>
    <text x="343" y="146" text-anchor="end">-168</text>
    <text x="357" y="172" text-anchor="end">-146</text>
    <text x="417" y="198" text-anchor="end">-48</text>
    <text x="543" y="225">139</text>
    <text x="568" y="251">180</text>
    <text x="658" y="277">328</text>
  </g>
  <g font-size="8" fill="var(--rose)" text-anchor="middle">
    <text x="208" y="305">-400</text><text x="269" y="305">-300</text><text x="330" y="305">-200</text><text x="391" y="305">-100</text>
    <text x="452" y="305">0</text><text x="513" y="305">100</text><text x="574" y="305">200</text><text x="635" y="305">300</text><text x="697" y="305">400</text>
  </g>
</svg>

<h2 class="abs claim" style="left:451px;top:408px">loneliness is worse than Tobacco!</h2>
<p class="abs finding">Individuals who reported feeling lonely reported greater<br>overall PD symptom severity (+328; p=0.000), which was<br>even higher than scores for smoking tobacco (+173;<br>p=0.005) and having a lot of stress (+180; p=0.000).</p>

<div class="abs vrule" style="left:860px;top:212px;height:307px"></div>

<h2 class="abs claim" style="left:877px;top:203px">lonliness is worse than tremor!</h2>
<p class="abs sub-head" style="left:877px;top:231px">quality of life Vs tremor</p>

<svg class="abs panel" style="left:877px;top:247px" width="235" height="126" viewBox="0 0 449 240" role="img" aria-label="Scatter plot of quality of life against tremor, R squared 0.0754">
  <g font-size="9" fill="var(--rose)" text-anchor="end">
    <text x="38" y="200">0</text><text x="38" y="169">10</text><text x="38" y="138">20</text><text x="38" y="107">30</text><text x="38" y="76">40</text><text x="38" y="45">50</text><text x="38" y="14">60</text>
  </g>
  <g font-size="9" fill="var(--rose)" text-anchor="middle">
    <text x="46" y="215">0</text><text x="123" y="215">20</text><text x="201" y="215">40</text><text x="278" y="215">60</text><text x="356" y="215">80</text><text x="433" y="215">100</text>
    <text x="240" y="233">Tremor</text>
  </g>
  <text transform="translate(15 105) rotate(-90)" font-size="8.5" fill="var(--rose)" text-anchor="middle">PROMIS Total - Quality of Life</text>
  <text x="395" y="36" font-size="9" fill="var(--rose)" text-anchor="middle">R² = 0.0754</text>
  <line x1="46" y1="10" x2="46" y2="197" stroke="#ddd"/>
  <g transform="translate(46 197) scale(3.87 -3.1)">
    <path d="M0 50 L40 50 L58 47 L72 42 L72 23 L50 21 L30 20 L0 22Z" fill="var(--rose)" opacity=".8"/>
    <path d="M2 28h0M5 24h0M8 33h0M12 22h0M15 27h0M18 45h0M22 26h0M25 19h0M28 35h0M31 24h0M34 29h0M37 46h0M40 21h0M42 33h0M45 27h0M48 42h0M50 22h0M52 38h0M55 30h0M57 45h0M60 26h0M62 34h0M64 20h0M66 40h0M68 28h0M70 32h0M72 24h0M74 38h0M76 30h0M79 27h0M82 33h0M85 36h0M88 25h0M90 31h0M93 22h0M96 40h0M98 41h0M100 30h0M20 15h0M24 13h0M8 16h0M58 17h0M36 14h0M85 22h0M78 35h0M82 28h0M92 35h0" stroke="var(--rose)" stroke-width="4" stroke-linecap="round" vector-effect="non-scaling-stroke" fill="none"/>
    <line x1="0" y1="39" x2="75" y2="32" stroke="var(--navy)" stroke-width="1.6" stroke-dasharray="2 2" vector-effect="non-scaling-stroke"/>
    <line x1="75" y1="32" x2="100" y2="30" stroke="var(--rose)" stroke-width="1.4" stroke-dasharray="2 2" vector-effect="non-scaling-stroke"/>
  </g>
</svg>

<p class="abs sub-head" style="left:877px;top:375px">quality of life Vs withdrawn</p>

<svg class="abs panel" style="left:877px;top:391px" width="232" height="125" viewBox="0 0 444 240" role="img" aria-label="Scatter plot of quality of life against social withdrawal, R squared 0.4872">
  <g font-size="9" fill="var(--rose)" text-anchor="end">
    <text x="40" y="194">0</text><text x="40" y="164">10</text><text x="40" y="135">20</text><text x="40" y="105">30</text><text x="40" y="75">40</text><text x="40" y="45">50</text><text x="40" y="15">60</text>
  </g>
  <g font-size="9" fill="var(--rose)" text-anchor="middle">
    <text x="50" y="209">0</text><text x="126" y="209">20</text><text x="201" y="209">40</text><text x="277" y="209">60</text><text x="352" y="209">80</text><text x="428" y="209">100</text>
    <text x="240" y="227">Withdrawn</text>
  </g>
  <text transform="translate(17 105) rotate(-90)" font-size="8.5" fill="var(--rose)" text-anchor="middle">PROMIS Total - Quality of Life</text>
  <text x="393" y="38" font-size="9" fill="var(--rose)" text-anchor="middle">R² = 0.4872</text>
  <line x1="50" y1="12" x2="50" y2="191" stroke="#ddd"/>
  <g transform="translate(50 191) scale(3.78 -2.98)">
    <path d="M0 50 L20 49 L50 42 L78 35 L78 22 L50 22 L20 28 L0 32Z" fill="var(--rose)" opacity=".8"/>
    <path d="M3 30h0M6 36h0M10 28h0M14 33h0M17 45h0M21 30h0M24 40h0M27 25h0M30 43h0M33 34h0M36 38h0M40 28h0M43 35h0M46 26h0M49 38h0M52 30h0M55 27h0M58 36h0M61 24h0M64 32h0M67 29h0M70 22h0M73 33h0M76 26h0M79 30h0M82 24h0M84 17h0M86 22h0M88 20h0M90 25h0M94 18h0M100 30h0M100 20h0M60 15h0M40 16h0M25 22h0M80 19h0M85 15h0" stroke="var(--rose)" stroke-width="4" stroke-linecap="round" vector-effect="non-scaling-stroke" fill="none"/>
    <line x1="0" y1="41" x2="78" y2="25" stroke="var(--navy)" stroke-width="1.6" stroke-dasharray="2 2" vector-effect="non-scaling-stroke"/>
    <line x1="78" y1="25" x2="100" y2="20" stroke="var(--rose)" stroke-width="1.4" stroke-dasharray="2 2" vector-effect="non-scaling-stroke"/>
  </g>
</svg>

<div class="abs hrule" style="left:450px;top:542px;width:688px"></div>

<svg class="abs panel" style="left:52px;top:552px" width="359" height="214" viewBox="0 0 686 408" role="img" aria-label="Scatter plot of PRO-PD score against years since diagnosis, shaded by quality of life band">
  <g class="cond" font-weight="600" font-size="19" fill="var(--navy)" text-anchor="middle">
    <text x="350" y="27">Correlation Between</text>
    <text x="350" y="54">Quality of Life and PRO-PD Score</text>
  </g>
  <text x="640" y="28" font-size="8" font-weight="700" fill="var(--navy)" text-anchor="middle">Harlow LK 2019</text>
  <rect x="17" y="73" width="35" height="283" fill="#dfe2e9"/>
  <text transform="translate(40 215) rotate(-90)" class="cond" font-size="19" font-weight="600" fill="var(--navy)" text-anchor="middle">PRO-PD Score</text>
  <rect x="101" y="73" width="396" height="113" fill="#b9bfcd"/>
  <rect x="101" y="186" width="396" height="55" fill="#e2e5ec"/>
  <rect x="101" y="241" width="396" height="57" fill="#cfd3dd"/>
  <rect x="101" y="298" width="396" height="55" fill="#e8eaef"/>
  <rect x="497" y="73" width="35" height="280" fill="#c9ced9"/>
  <text transform="translate(522 215) rotate(-90)" class="cond" font-size="19" font-weight="600" fill="var(--navy)" text-anchor="middle">Quality of Life</text>
  <rect x="532" y="73" width="107" height="113" fill="#b9bfcd"/>
  <rect x="532" y="186" width="107" height="55" fill="#e2e5ec"/>
  <rect x="532" y="241" width="107" height="57" fill="#cfd3dd"/>
  <rect x="532" y="298" width="107" height="55" fill="#e8eaef"/>
  <g class="cond" font-size="19" font-weight="600" fill="var(--navy)" text-anchor="middle">
    <text x="580" y="131">Poor</text><text x="580" y="211">Fair</text><text x="580" y="268">Good</text><text x="580" y="325">Excellent</text>
  </g>
  <g font-size="13" fill="#333" text-anchor="end">
    <text x="90" y="81">2500</text><text x="90" y="137">2000</text><text x="90" y="192">1500</text><text x="90" y="247">1000</text><text x="90" y="303">500</text><text x="90" y="358">0</text>
  </g>
  <g font-size="13" fill="#333" text-anchor="middle">
    <text x="178" y="378">5</text><text x="255" y="378">10</text><text x="332" y="378">15</text><text x="409" y="378">20</text><text x="486" y="378">25</text><text x="563" y="378">30</text><text x="640" y="378">35</text>
    <text x="370" y="399" font-size="14">Years Since Diagnosis</text>
  </g>
  <g transform="translate(101 353) scale(15.4 -0.1108)">
    <path d="M0 0 L0 2100 L4 2000 L8 1700 L11 1350 L14 950 L12 500 L8 150 L4 0Z" fill="#3d4f73" opacity=".55"/>
    <path d="M1 2350h0M2 2100h0M3 1900h0M4 2250h0M5 1700h0M6 2000h0M7 1850h0M8 2200h0M9 1950h0M10 2150h0M11 1750h0M12 2050h0M13 1600h0M14 1850h0M15 1700h0M16 1550h0M17 1450h0M18 1300h0M19 1650h0M20 1200h0M21 1100h0M22 1400h0M23 950h0M24 1250h0M25 1500h0M26 1650h0M27 1550h0M3 1200h0M6 1400h0M9 1500h0M12 1350h0M14 1100h0M16 1000h0M18 900h0M20 800h0M22 700h0M24 550h0M15 600h0M11 700h0M10 400h0M13 300h0M20 1750h0M18 2100h0M22 1950h0M24 1900h0M5 500h0M7 300h0M19 100h0M29 1700h0M17 800h0M21 1500h0" stroke="#2e3c5c" stroke-width="4" stroke-linecap="round" vector-effect="non-scaling-stroke" fill="none"/>
    <line x1="0" y1="500" x2="29" y2="1700" stroke="#4b5a78" stroke-width="2" vector-effect="non-scaling-stroke"/>
  </g>
</svg>

<svg class="abs panel" style="left:454px;top:563px" width="298" height="202" viewBox="0 0 570 386" role="img" aria-label="PRO-PD score by years since diagnosis for lonely and not lonely groups">
  <line x1="64" y1="10" x2="64" y2="319" stroke="#999"/>
  <line x1="64" y1="319" x2="540" y2="319" stroke="#999"/>
  <g font-size="10" font-weight="700" fill="#222" text-anchor="end">
    <text x="56" y="322">0</text><text x="56" y="279">200</text><text x="56" y="236">400</text><text x="56" y="193">600</text><text x="56" y="149">800</text><text x="56" y="106">1000</text><text x="56" y="63">1200</text><text x="56" y="20">1400</text>
  </g>
  <text transform="translate(24 166) rotate(-90)" font-size="10" font-weight="700" text-anchor="middle">PRO-PD</text>
  <g font-size="10" font-weight="700" fill="#222" text-anchor="middle">
    <text x="88" y="337">0</text><text x="132" y="337">1</text><text x="175" y="337">2</text><text x="219" y="337">3</text><text x="262" y="337">4</text><text x="306" y="337">5</text><text x="350" y="337">6</text><text x="393" y="337">7</text><text x="437" y="337">8</text><text x="480" y="337">9</text><text x="524" y="337">10</text>
    <text x="306" y="354" font-size="11">Years Since Diagnosis</text>
  </g>
  <polyline points="88,112.7 131.6,129 175.2,111.3 218.8,118.8 262.4,91.9 306,64.5 349.6,37.7 393.2,64.5 436.8,94 480.4,34.5 524,32.1" fill="none" stroke="var(--rose-soft)" stroke-width="2.5"/>
  <polyline points="88,202.7 131.6,186.1 175.2,188.9 218.8,172.1 262.4,174.9 306,169.9 349.6,144.7 393.2,133.9 436.8,125.9 480.4,114.7 524,108.7" fill="none" stroke="var(--navy-deep)" stroke-width="2.5"/>
  <g font-size="8.5" font-weight="700" fill="#222">
    <text x="98" y="110">961</text><text x="124" y="142">881</text><text x="184" y="109">963</text><text x="229" y="130">928</text><text x="272" y="90">1053</text><text x="300" y="62">1180</text><text x="360" y="40">1304</text><text x="403" y="62">1180</text><text x="446" y="102">1043</text><text x="458" y="37">1319</text><text x="531" y="35">1330</text>
    <text x="98" y="209">539</text><text x="136" y="191">616</text><text x="182" y="196">603</text><text x="225" y="178">681</text><text x="266" y="182">668</text><text x="312" y="179">691</text><text x="355" y="150">808</text><text x="400" y="142">858</text><text x="444" y="132">895</text><text x="482" y="124">947</text><text x="530" y="112">975</text>
  </g>
  <g font-size="9" font-weight="700" fill="#222">
    <line x1="215" y1="368" x2="238" y2="368" stroke="var(--rose-soft)" stroke-width="2.5"/><text x="241" y="371">LONELY</text>
    <line x1="300" y1="368" x2="323" y2="368" stroke="var(--navy-deep)" stroke-width="2.5"/><text x="326" y="371">NOT LONELY</text>
  </g>
</svg>

<p class="abs summary">Overall, Individuals<br>identifying as<br>being lonely reported<br>constantly greater PD<br>symptom severity.</p>

<div class="abs brand"><span class="dot"></span><span class="name">Cedarbrook<br>University</span></div>

</body>
</html>
```